Retail Flooring Business Monthly Flyer

I need a flyer design for a retail flooring buiness based in North Vancouver, BC that caters to the lower mainland market place.

The company sales & installs all type of flooring.(hardwood, laminate, carpet, tile, epoxy flooring) as well as small renovations (kitchens, & bathroom renovations). Our current logo is blue red & white and can be seen on the following website: www.larkhavenfloors.com

I would like to create a flyer that will target a mid to high end customer base. The flyer should also carry our monthly specials. We want to use the same logo.

The flyer should be simple, clean, & modern. We are open to all of your creativity.

Target Market(s)

30-65 years old homeowners mid to high end

Industry/Entity Type

Retail

Requirements
Must have
• Must have:
- Monthly specials
- Current Logo
Specials:
- Wide Plank Oak $6.49
- Brushed Oak $5.99
- Canadian Maple (4 colours) $6.49
- Asian Maple ( 1 colour left) $4.49
- Royal Sapele $6.29
- Natural Jatoba $6.29
- Bamboo Click (2 colours left) $4.99
- Bamboo T&G (1 colour left) $4.49

```html
<!DOCTYPE html>
<html lang="en">
<head>
<meta charset="utf-8">
<title>Larkhaven Floors – Monthly Specials Flyer</title>
<link rel="stylesheet" href="https://fonts.googleapis.com/css2?family=Lobster&family=Oswald:wght@600&family=Roboto:wght@400;700&display=swap">
<style>
  :root {
    --stage: #1c1c1c;
    --brand-red: #a3121c;
    --deep-red: #7d0d14;
    --burnt-orange: #d9551f;
    --gold: #f0a020;
    --white: #ffffff;
    --ink: #111111;
    --wood-light: #b9794a;
    --wood-dark: #5a2f18;
    --window-blue: #8fb6d8;
  }
  * { box-sizing: border-box; margin: 0; padding: 0; }
  html, body { width: 1200px; height: 800px; overflow: hidden; }
  body {
    background: var(--stage);
    font-family: "Roboto", Arial, sans-serif;
    position: relative;
  }

  .flyer {
    position: absolute;
    top: 215px;
    width: 555px;
    height: 370px;
    overflow: hidden;
  }

  /* Front side */
  .flyer--front { left: 30px; background: var(--brand-red); }
  .front-photo {
    position: absolute;
    left: 70px; top: 0; right: 0; bottom: 0;
    background:
      linear-gradient(180deg, rgba(143,182,216,0) 0%, rgba(143,182,216,0) 100%),
      linear-gradient(160deg, #6b3a20 0%, var(--wood-light) 40%, #d9c6a8 62%, var(--window-blue) 80%, #e6dccb 100%);
  }
  .order-band {
    position: absolute;
    left: 0; top: 0; bottom: 0;
    width: 70px;
    background: var(--brand-red);
    border-right: 3px solid var(--gold);
  }
  .order-text {
    position: absolute;
    left: 35px; top: 185px;
    transform: translate(-50%, -50%) rotate(-90deg);
    white-space: nowrap;
    color: var(--white);
    text-align: center;
    line-height: 1.05;
  }
  .order-text .label { display: block; font-weight: 700; font-size: 14px; letter-spacing: 1px; color: var(--ink); }
  .order-text .phone { display: block; font-size: 26px; font-weight: 400; }
  .sale-tag {
    position: absolute;
    top: 0; right: 70px;
    width: 78px; height: 64px;
    background: var(--brand-red);
    color: var(--white);
    font-family: "Oswald", Impact, sans-serif;
    font-size: 24px;
    display: flex; align-items: center; justify-content: center;
    box-shadow: 0 2px 0 var(--deep-red);
  }
  .front-wave { position: absolute; left: 70px; right: 0; bottom: 0; height: 130px; }
  .front-title {
    position: absolute;
    left: 150px; bottom: 58px;
    font-family: "Lobster", cursive;
    font-size: 44px;
    color: var(--gold);
    transform: rotate(6deg);
  }
  .brand-mark {
    position: absolute;
    right: 22px; bottom: 14px;
    display: flex; align-items: center; gap: 6px;
    font-family: "Roboto", Arial, sans-serif;
    font-size: 14px;
    font-weight: 400;
    color: var(--white);
    letter-spacing: 1px;
  }
  .brand-mark .square { width: 10px; height: 10px; background: var(--white); }

  /* Back side */
  .flyer--back { right: 30px; background: var(--white); }
  .address-area { height: 150px; background: var(--white); }
  .contact-strip {
    height: 28px;
    background: var(--brand-red);
    color: var(--white);
    font-size: 10px;
    display: flex; align-items: center; gap: 22px;
    padding: 0 16px;
  }
  .contact-strip span { display: flex; align-items: center; gap: 5px; }
  .specials-panel {
    position: relative;
    height: 192px;
    background: var(--burnt-orange);
    padding: 16px 0 0 16px;
  }
  .specials-title {
    position: absolute;
    right: 18px; top: 28px;
    color: var(--white);
    text-align: right;
    font-family: "Lobster", cursive;
    line-height: 1;
  }
  .specials-title .month { display: block; font-size: 40px; }
  .specials-title .sub { display: block; font-size: 20px; }
  .specials-grid {
    display: grid;
    grid-template-columns: repeat(4, 84px);
    gap: 10px 8px;
  }
  .special-item { background: var(--ink); padding: 3px; }
  .special-photo {
    height: 46px;
    background: linear-gradient(135deg, var(--wood-dark), var(--wood-light) 60%, #e2cfae);
  }
  .special-name { color: var(--white); font-size: 8px; margin-top: 3px; white-space: nowrap; overflow: hidden; }
  .special-price { color: var(--gold); font-size: 9px; font-weight: 700; }
</style>
</head>
<body>

<section class="flyer flyer--front">
  <div class="front-photo" role="img" aria-label="Photo of a bright modern kitchen and dining room with a warm hardwood floor and large windows"></div>
  <div class="order-band">
    <div class="order-text"><span class="label">ORDER NOW:</span><span class="phone">604 555 0142</span></div>
  </div>
  <div class="sale-tag">SALE</div>
  <svg class="front-wave" viewBox="0 0 485 130" preserveAspectRatio="none" aria-hidden="true">
    <path d="M0 20 C140 60 300 90 485 70 L485 130 L0 130 Z" fill="#a3121c"/>
    <path d="M0 20 C140 60 300 90 485 70" fill="none" stroke="#f0a020" stroke-width="2"/>
  </svg>
  <div class="front-title">Monthly Specials</div>
  <div class="brand-mark"><span class="square"></span>larkhaven floors</div>
</section>

<section class="flyer flyer--back">
  <div class="address-area"></div>
  <div class="contact-strip">
    <span>
      <svg width="10" height="8" viewBox="0 0 10 8" aria-hidden="true"><rect x="0.5" y="0.5" width="9" height="7" fill="none" stroke="#fff"/><path d="M0.5 0.5 L5 4.5 L9.5 0.5" fill="none" stroke="#fff"/></svg>
      contact@larkhavenfloors.com
    </span>
    <span>
      <svg width="9" height="9" viewBox="0 0 10 10" aria-hidden="true"><circle cx="5" cy="5" r="4.3" fill="none" stroke="#fff"/><path d="M0.7 5 H9.3 M5 0.7 V9.3" stroke="#fff"/></svg>
      www.larkhavenfloors.com
    </span>
    <span>
      <svg width="8" height="10" viewBox="0 0 8 10" aria-hidden="true"><rect x="1" y="0.5" width="6" height="9" rx="1" fill="none" stroke="#fff"/></svg>
      604 555 0142
    </span>
  </div>
  <div class="specials-panel">
    <div class="specials-grid">
      <div class="special-item"><div class="special-photo" role="img" aria-label="Wide plank oak flooring in a room"></div><div class="special-name">Wide Plank Oak</div><div class="special-price">$6.49</div></div>
      <div class="special-item"><div class="special-photo" role="img" aria-label="Brushed oak flooring in a room"></div><div class="special-name">Brushed Oak</div><div class="special-price">$5.99</div></div>
      <div class="special-item"><div class="special-photo" role="img" aria-label="Canadian maple flooring in a room"></div><div class="special-name">Canadian Maple</div><div class="special-price">$6.49</div></div>
      <div class="special-item"><div class="special-photo" role="img" aria-label="Asian maple flooring in a room"></div><div class="special-name">Asian Maple</div><div class="special-price">$4.49</div></div>
      <div class="special-item"><div class="special-photo" role="img" aria-label="Royal sapele flooring in a room"></div><div class="special-name">Royal Sapele</div><div class="special-price">$6.29</div></div>
      <div class="special-item"><div class="special-photo" role="img" aria-label="Natural jatoba flooring in a room"></div><div class="special-name">Natural Jatoba</div><div class="special-price">$6.29</div></div>
      <div class="special-item"><div class="special-photo" role="img" aria-label="Bamboo click flooring in a room"></div><div class="special-name">Bamboo Click</div><div class="special-price">$4.99</div></div>
      <div class="special-item"><div class="special-photo" role="img" aria-label="Bamboo tongue and groove flooring in a room"></div><div class="special-name">Bamboo T&amp;G</div><div class="special-price">$4.49</div></div>
    </div>
    <div class="specials-title"><span class="month">December</span><span class="sub">Monthly Specials</span></div>
  </div>
</section>

</body>
</html>
```